Brookvane Counsel Partners Website Design

I need a website design for my new business consulting and executive coaching firm, Brookvane Counsel Partners. We provide consultative services to business C-suites as well as personal coaching to executives. I have attached the logo with color scheme I have chosen. I would like the website to reflect professionalism and continue the color scheme in the logo.

Target Market(s)

Small to medium business and their executives; middle to upper income men and women in mid- to late career looking for significance

Industry/Entity Type

Business Consultant

Number of Pages Required

4 page

Requirements
Must have
• A homepage with prominent logo and way to contact for more information; an area on the homepage with easy to read, clear text to describe what the company does; a prominent area on the homepage for a tagline; a blog page that can be updated regularly, an "about us" page with biographical information; an "about us" page; a page detailing services offered
• The web design must match the logo colors and font that I have uploaded.
Nice to have
• A lighthouse picture in the background or header
Should not have
• A lot of text area on the homepage

```html
<!DOCTYPE html>
<html lang="en">
<head>
<meta charset="utf-8">
<title>Brookvane Counsel Partners</title>
<link href="https://fonts.googleapis.com/css2?family=Roboto+Condensed:wght@300;400;700&family=Open+Sans:ital,wght@0,400;0,600;1,400&display=swap" rel="stylesheet">
<style>
:root{
  --navy:#1d2b63;
  --navy-deep:#172250;
  --sky:#4a6aa8;
  --red:#8a1515;
  --red-dark:#7a1111;
  --ink:#333;
  --muted:#666;
  --light:#f1f1f1;
  --footer:#1b1b1b;
  --footer-text:#9a9a9a;
  --white:#fff;
}
*{margin:0;padding:0;box-sizing:border-box}
html,body{width:1200px;height:2553px;overflow:hidden}
body{position:relative;font-family:"Open Sans",Arial,sans-serif;color:var(--ink);background:var(--white)}
.abs{position:absolute}
.cond{font-family:"Roboto Condensed","Arial Narrow",sans-serif}

/* hero */
.hero{position:absolute;left:0;top:0;width:1200px;height:667px;overflow:hidden}
.hero-bg{position:absolute;inset:0;background:linear-gradient(180deg,#2f4a8e 0%,#4866a6 40%,#5b78b2 55%,#31527f 62%,#9a9a98 80%,#c9c8c4 100%)}
.brand{left:99px;top:52px;width:170px;text-align:center;color:var(--white);font-family:"Roboto Condensed",sans-serif;font-size:19px;font-weight:400;letter-spacing:1px;line-height:1.15;text-transform:uppercase}
.nav{left:393px;top:34px;display:flex;gap:0}
.nav a{color:var(--white);text-decoration:none;font-family:"Roboto Condensed",sans-serif;font-size:14px;padding:6px 16px;margin-right:13px;border:1px solid transparent;letter-spacing:.3px}
.nav a.active{border-color:rgba(255,255,255,.8)}
.contact-top{right:145px;top:27px;text-align:right;color:var(--white);font-size:14px;line-height:21px}
.phone-ring{left:1068px;top:30px;width:33px;height:33px;border:1.5px solid var(--white);border-radius:50%}
.hero-title{left:98px;top:288px;color:var(--white);font-family:"Roboto Condensed",sans-serif;font-weight:700;font-size:50px;line-height:52px;text-transform:uppercase;letter-spacing:.5px}
.hero-sub{left:98px;top:400px;color:var(--white);font-family:"Roboto Condensed",sans-serif;font-size:20px;line-height:23px}
.hero-arrows{left:97px;top:464px;display:flex;gap:7px}
.hero-arrows span{width:34px;height:34px;border:1.5px solid var(--white);border-radius:50%;display:flex;align-items:center;justify-content:center}

/* welcome */
.welcome{position:absolute;left:0;top:667px;width:1200px;height:237px;text-align:center}
.welcome h2{margin-top:50px;font-family:"Roboto Condensed",sans-serif;font-weight:400;font-size:31px;color:var(--navy);letter-spacing:.5px}
.welcome h2 b{font-weight:400}
.divider{margin:14px auto 0;width:230px;height:16px;position:relative}
.divider::before{content:"";position:absolute;left:0;right:0;top:8px;height:1px;background:#ccc}
.divider::after{content:"";position:absolute;left:108px;top:1px;width:14px;height:14px;background:#999;transform:rotate(45deg)}
.welcome p{width:925px;margin:20px auto 0;font-size:11.5px;line-height:22px;color:var(--muted)}

/* services */
.services{position:absolute;left:0;top:904px;width:1200px;height:512px;overflow:hidden;color:var(--white)}
.services-bg{position:absolute;inset:0;background:linear-gradient(90deg,#27356c 0%,#34437a 45%,#3f4f85 70%,#2b3a70 100%)}
.notch{position:absolute;left:565px;top:0;width:0;height:0;border-left:36px solid transparent;border-right:36px solid transparent;border-top:41px solid var(--white)}
.services h2{position:absolute;left:0;width:1200px;top:83px;text-align:center;font-family:"Roboto Condensed",sans-serif;font-weight:400;font-size:31px;letter-spacing:.5px}
.services .rule{position:absolute;left:561px;top:133px;width:78px;height:2px;background:var(--white)}
.svc{position:absolute;width:230px;text-align:center}
.svc h3{font-family:"Roboto Condensed",sans-serif;font-weight:400;font-size:17px;text-transform:uppercase;letter-spacing:.3px;margin-bottom:6px}
.svc p{font-size:11.5px;line-height:20px}
.tri{position:absolute}
.side-arrow{position:absolute;top:234px}

/* provide */
.monitor{left:179px;top:1477px;width:357px;height:341px}
.provide{left:589px;top:1500px;width:440px}
.provide h2{font-family:"Roboto Condensed",sans-serif;font-weight:400;font-size:52px;line-height:56px;color:var(--navy)}
.provide h4{font-family:"Roboto Condensed",sans-serif;font-weight:400;font-size:16px;line-height:20px;color:var(--navy-deep);margin-top:4px}
.provide p{font-size:11.5px;line-height:21px;color:var(--muted);margin-top:14px}
.ticks{list-style:none;margin-top:14px}
.ticks li{font-size:11.5px;color:var(--muted);height:30px;display:flex;align-items:center;gap:14px}

/* testimonial */
.testimonial{position:absolute;left:0;top:1915px;width:1200px;height:315px;background:var(--light);text-align:center}
.quote-tab{position:absolute;left:565px;top:-24px;width:70px;height:50px;border-radius:35px;background:var(--light);color:#aaa;font-family:Georgia,serif;font-size:26px;line-height:54px}
.avatar{position:absolute;left:551px;top:52px;width:96px;height:96px;border-radius:50%;border:4px solid var(--white);background:radial-gradient(circle at 50% 40%,#8a9bb0,#3c4a5c)}
.testimonial blockquote{position:absolute;left:160px;top:155px;width:880px;font-style:italic;font-size:12.5px;line-height:25.5px;color:#777}
.testimonial .who{position:absolute;left:0;width:1200px;top:248px;font-size:15px;color:#555}
.testimonial .who b{color:var(--red);font-weight:600}

/* footer */
.footer{position:absolute;left:0;top:2230px;width:1200px;height:262px;background:var(--footer);color:var(--footer-text)}
.footer h5{font-family:"Open Sans",sans-serif;font-weight:400;font-size:14.5px;color:#ddd;letter-spacing:.3px;text-transform:uppercase}
.f-brand{left:96px;top:138px;width:165px;text-align:center;color:#555;font-family:"Roboto Condensed",sans-serif;font-size:19px;line-height:1.15;text-transform:uppercase;letter-spacing:1px}
.f-links{left:323px;top:43px}
.f-links ul{list-style:none;margin-top:18px}
.f-links li{font-size:12px;line-height:24px;color:#bbb}
.f-sep{top:42px;width:1px;height:150px;background:#333}
.f-news{left:545px;top:43px;width:220px}
.f-news p{font-size:11px;line-height:19px;margin-top:12px;color:#999}
.field{position:absolute;background:var(--white);color:#333;font-size:11px;padding:0 12px;display:flex;align-items:center}
.subscribe{position:absolute;left:667px;top:177px;width:97px;height:41px;background:var(--red);color:var(--white);font-size:12px;display:flex;align-items:center;justify-content:center}
.f-touch{left:875px;top:45px}
.f-touch .addr{font-size:12.5px;line-height:20px;margin-top:18px}
.f-touch .row{display:flex;align-items:center;gap:14px;font-size:13px;margin-top:12px}
.socials{display:flex;gap:6px;margin-top:12px}
.socials span{width:26px;height:26px;border:1.3px solid #aaa;border-radius:50%}
.copyright{position:absolute;left:0;top:2492px;width:1200px;height:61px;background:var(--red-dark);color:#eee;font-size:12.5px;display:flex;align-items:center;justify-content:center}
</style>
</head>
<body>

<header class="hero">
  <div class="hero-bg" role="img" aria-label="Photograph of a white lighthouse with a red lantern on rocky coastline under a blue sky, a small boat on the sea"></div>
  <div class="abs brand">Brookvane Counsel<br>Partners</div>
  <nav class="abs nav">
    <a class="active">HOME</a><a>ABOUT US</a><a>SERVICES</a><a>CONTACT US</a>
  </nav>
  <div class="abs contact-top">+1 555 204 7310<br>info@brookvanecounsel.com</div>
  <div class="abs phone-ring">
    <svg width="30" height="30" viewBox="0 0 30 30"><path d="M11 9c1 0 2 2.5 2 3s-1.3 1.2-1.3 1.8 2.5 3.8 3.5 4 1.2-1.3 1.8-1.3 3 1 3 2-1.5 2-2.5 2C13 20.5 9.5 16.5 9 12.5 8.8 10.5 10 9 11 9z" fill="#fff"/></svg>
  </div>
  <h1 class="abs hero-title">Brookvane<br>Counsel Partners</h1>
  <p class="abs hero-sub">We provide consultative services to business C-suites<br>as well as personal coaching to executives.</p>
  <div class="abs hero-arrows">
    <span><svg width="14" height="14" viewBox="0 0 14 14"><path d="M12 7H2M6 3 2 7l4 4" stroke="#fff" stroke-width="1.6" fill="none"/></svg></span>
    <span><svg width="14" height="14" viewBox="0 0 14 14"><path d="M2 7h10M8 3l4 4-4 4" stroke="#fff" stroke-width="1.6" fill="none"/></svg></span>
  </div>
</header>

<section class="welcome">
  <h2>WELCOME TO <b>BROOKVANE COUNSEL PARTNERS</b></h2>
  <div class="divider"></div>
  <p>Lorem ipsum dolor sit amet, consectetur adipiscing elit, sed do eiusmod tempor incididunt ut labore et dolore magna aliqua. Ut enim ad minim veniam, quis nostrud exercitation ullamco laboris nisi ut aliquip ex ea commodo consequat. Duis aute irure dolor in reprehenderit in voluptate velit esse cillum dolore eu fugiat nulla pariatur. Excepteur sint occaecat cupidatat non proident, sunt in culpa qui officia deserunt mollit anim id est laborum</p>
</section>

<section class="services">
  <div class="services-bg" role="img" aria-label="Blurred photograph of a smiling businesswoman with colleagues in an office, tinted navy blue"></div>
  <div class="notch"></div>
  <h2>CONSULTATIVE SERVICES</h2>
  <div class="rule"></div>

  <svg class="side-arrow" style="left:34px" width="20" height="44" viewBox="0 0 20 44"><path d="M18 2 2 22l16 20" stroke="#fff" stroke-opacity=".7" stroke-width="1.4" fill="none"/></svg>
  <svg class="side-arrow" style="left:1140px" width="20" height="44" viewBox="0 0 20 44"><path d="M2 2l16 20L2 42" stroke="#fff" stroke-opacity=".7" stroke-width="1.4" fill="none"/></svg>

  <!-- business consulting -->
  <svg class="tri" style="left:132px;top:194px" width="160" height="140" viewBox="0 0 160 140">
    <path d="M80 2 158 138H2z" stroke="#fff" stroke-width="2" fill="none"/>
    <rect x="67" y="82" width="27" height="18" rx="2" stroke="#fff" stroke-width="3" fill="none"/>
    <path d="M80 100v5M72 107h16" stroke="#fff" stroke-width="3"/>
  </svg>
  <div class="svc" style="left:96px;top:346px"><h3>Business Consulting</h3><p>Lorem ipsum dolor sit amet, consectetur adipiscing elit, sed do eiusmod tempor incididunt ut labore et dolore</p></div>

  <!-- executive coaching -->
  <svg class="tri" style="left:388px;top:293px" width="160" height="140" viewBox="0 0 160 140">
    <path d="M80 2 158 138H2z" stroke="#fff" stroke-width="2" fill="none"/>
    <rect x="78" y="72" width="18" height="14" stroke="#fff" stroke-width="2" fill="none"/>
    <circle cx="70" cy="76" r="3" fill="#fff"/><path d="M70 80v10M70 82l8-6" stroke="#fff" stroke-width="2.5"/>
    <circle cx="64" cy="98" r="3" fill="#fff"/><circle cx="76" cy="98" r="3" fill="#fff"/><circle cx="88" cy="98" r="3" fill="#fff"/><circle cx="100" cy="98" r="3" fill="#fff"/>
    <path d="M60 108h44" stroke="#fff" stroke-width="5"/>
  </svg>
  <div class="svc" style="left:353px;top:194px"><h3>Executive Coaching</h3><p>Lorem ipsum dolor sit amet, consectetur adipiscing elit, sed do eiusmod tempor incididunt ut labore et dolore</p></div>

  <!-- business c-suites -->
  <svg class="tri" style="left:652px;top:194px" width="160" height="140" viewBox="0 0 160 140">
    <path d="M80 2 158 138H2z" stroke="#fff" stroke-width="2" fill="none"/>
    <circle cx="74" cy="92" r="7" stroke="#fff" stroke-width="5" stroke-dasharray="3 2.5" fill="none"/>
    <circle cx="89" cy="82" r="4.5" stroke="#fff" stroke-width="3.5" stroke-dasharray="2 2" fill="none"/>
    <circle cx="89" cy="100" r="4" stroke="#fff" stroke-width="3" stroke-dasharray="2 2" fill="none"/>
  </svg>
  <div class="svc" style="left:617px;top:346px"><h3>Business C-Suites</h3><p>Lorem ipsum dolor sit amet, consectetur adipiscing elit, sed do eiusmod tempor incididunt ut labore et dolore</p></div>

  <!-- personal coaching -->
  <svg class="tri" style="left:911px;top:293px" width="160" height="140" viewBox="0 0 160 140">
    <path d="M80 2 158 138H2z" stroke="#fff" stroke-width="2" fill="none"/>
    <circle cx="80" cy="76" r="8" stroke="#fff" stroke-width="2" fill="none"/>
    <path d="M64 108v-8c0-8 7-12 16-12s16 4 16 12v8z" stroke="#fff" stroke-width="2" fill="none"/>
    <path d="M80 88v14" stroke="#fff" stroke-width="2"/>
  </svg>
  <div class="svc" style="left:876px;top:194px"><h3>Personal Coaching</h3><p>Lorem ipsum dolor sit amet, consectetur adipiscing elit, sed do eiusmod tempor incididunt ut labore et dolore</p></div>
</section>

<div class="abs monitor">
  <div style="position:absolute;left:0;top:0;width:357px;height:265px;border-radius:10px;background:#1a1a1a;padding:14px 14px 36px">
    <div role="img" aria-label="Photograph of a business team gathered at a whiteboard shown on a desktop monitor" style="width:100%;height:100%;background:linear-gradient(135deg,#cfe0ec,#9fb8cc 55%,#e4c9b0)"></div>
  </div>
  <div style="position:absolute;left:0;top:226px;width:357px;height:39px;border-radius:0 0 10px 10px;background:linear-gradient(#e8e8e8,#c9c9c9)"></div>
  <div style="position:absolute;left:132px;top:265px;width:94px;height:58px;background:linear-gradient(90deg,#b5b5b5,#e6e6e6,#b5b5b5)"></div>
  <div style="position:absolute;left:116px;top:320px;width:126px;height:8px;border-radius:4px;background:#c7c7c7"></div>
</div>

<section class="abs provide">
  <h2>WE PROVIDE</h2>
  <h4>Consultative Services To Business C-suites As Well As Personal Coaching To Executives</h4>
  <p>Lorem ipsum dolor sit amet, consectetur adipiscing elit, sed do eiusmod tempor incididunt ut labore et dolore magna aliqua. Ut enim ad minim veniam, quis nostrud exercitation ullamco laboris nisi ut aliquip</p>
  <ul class="ticks">
    <li><svg width="12" height="10" viewBox="0 0 12 10"><path d="M1 5l3.5 3.5L11 1.5" stroke="#1d2b63" stroke-width="2.2" fill="none"/></svg>Nemo enim ipsam voluptatem</li>
    <li><svg width="12" height="10" viewBox="0 0 12 10"><path d="M1 5l3.5 3.5L11 1.5" stroke="#1d2b63" stroke-width="2.2" fill="none"/></svg>Neque porro quisquam est, qui dolorem</li>
    <li><svg width="12" height="10" viewBox="0 0 12 10"><path d="M1 5l3.5 3.5L11 1.5" stroke="#1d2b63" stroke-width="2.2" fill="none"/></svg>Sed ut perspiciatis unde omnis iste</li>
    <li><svg width="12" height="10" viewBox="0 0 12 10"><path d="M1 5l3.5 3.5L11 1.5" stroke="#1d2b63" stroke-width="2.2" fill="none"/></svg>Nemo enim ipsam voluptatem</li>
    <li><svg width="12" height="10" viewBox="0 0 12 10"><path d="M1 5l3.5 3.5L11 1.5" stroke="#1d2b63" stroke-width="2.2" fill="none"/></svg>Neque porro quisquam</li>
  </ul>
</section>

<section class="testimonial">
  <div class="quote-tab">&ldquo;</div>
  <div class="avatar" role="img" aria-label="Portrait photograph of the client giving the testimonial"></div>
  <blockquote>&ldquo; Lorem ipsum dolor sit amet, consectetur adipiscing elit, sed do eiusmod tempor incididunt ut labore et dolore magna aliqua. Ut enim ad minim veniam, quis nostrud exercitation ullamco laboris nisi ut aliquip ex ea commodo consequat. Duis aute irure dolor in reprehenderit in voluptate velit esse cillum dolore eu fugiat nulla pariatur. Excepteur sint occaecat &rdquo;</blockquote>
  <div class="who"><b>Daniel Reeve</b> - Manager</div>
</section>

<footer class="footer">
  <div class="abs f-brand">Brookvane Counsel<br>Partners</div>
  <div class="abs f-links">
    <h5>Quick Links</h5>
    <ul><li>Home</li><li>About Us</li><li>Events</li><li>What we do</li><li>Contact Us</li></ul>
  </div>
  <div class="abs f-sep" style="left:471px"></div>
  <div class="abs f-news">
    <h5>Sign up for newsletter</h5>
    <p>Excepteur sint occaecat cupidatat non proident, sunt in culpa qui</p>
  </div>
  <div class="field" style="left:545px;top:126px;width:219px;height:40px">Enter Name</div>
  <div class="field" style="left:545px;top:177px;width:122px;height:41px">Enter Email</div>
  <div class="subscribe">SUBSCRIBE</div>
  <div class="abs f-sep" style="left:824px"></div>
  <div class="abs f-touch">
    <h5>Get in touch</h5>
    <div class="addr">Brookvane Counsel Partners<br>48 Harbour Lane, Westford</div>
    <div class="row"><svg width="16" height="16" viewBox="0 0 16 16"><path d="M3.5 1.5c1 0 2 2.5 2 3s-1.3 1.2-1.3 1.8 2.5 4 3.5 4.2 1.3-1.3 1.8-1.3 3 1 3 2-1.5 2.5-2.5 2.5C5.5 13.7 1.8 9.8 1.5 5.5 1.3 3 2.5 1.5 3.5 1.5z" stroke="#aaa" stroke-width="1.2" fill="none"/></svg>+1 555 318 6620</div>
    <div class="row"><svg width="16" height="12" viewBox="0 0 16 12"><rect x=".7" y=".7" width="14.6" height="10.6" stroke="#aaa" stroke-width="1.2" fill="none"/><path d="M1 1l7 6 7-6" stroke="#aaa" stroke-width="1.2" fill="none"/></svg>info@brookvanecounsel.com</div>
    <div class="socials"><span></span><span></span><span></span><span></span><span></span></div>
  </div>
</footer>

<div class="copyright">Copyright &copy; All Rights Reserved. Brookvane Counsel Partners</div>

</body>
</html>
```